Updates

Please take these words out of the flyer " or any other fees whatsoever." Added Monday, August 8, 2016

Industry/Entity Type

Real Estate

Font styles to use
Serif

Requirements
Must have

```html
<!DOCTYPE html>
<html lang="en">
<head>
<meta charset="utf-8">
<title>Summit Keystone Realty – Commission Plans Flyer</title>
<link rel="stylesheet" href="https://fonts.googleapis.com/css2?family=Arimo:wght@400;700&family=Roboto+Condensed:wght@700&display=swap">
<style>
  :root {
    --backdrop: #b3b3b3;
    --paper: #ffffff;
    --brand-red: #d3161f;
    --brand-red-bright: #e8121b;
    --brand-red-deep: #c21a22;
    --slate: #67686b;
    --slate-light: #8e8f92;
    --ink-white: #ffffff;
    --ink-dark: #222222;
  }
  * { box-sizing: border-box; margin: 0; padding: 0; }
  html, body { width: 900px; height: 1200px; overflow: hidden; }
  body {
    background: var(--backdrop);
    font-family: "Arimo", Arial, sans-serif;
    position: relative;
  }
  .flyer {
    position: absolute;
    left: 140px; top: 158px;
    width: 628px; height: 887px;
    background: var(--paper);
    overflow: hidden;
    box-shadow: 0 0 6px rgba(0,0,0,0.15);
  }
  .flyer-shapes { position: absolute; inset: 0; }
  .hero-artwork {
    position: absolute; left: 152px; top: 32px; width: 328px; height: 250px;
    border-radius: 4px;
    background: linear-gradient(180deg, var(--slate-light) 0%, var(--slate) 62%, var(--brand-red-deep) 100%);
  }
  .centered { position: absolute; left: 0; width: 628px; text-align: center; color: var(--ink-white); }
  .company-name { top: 314px; font-size: 28px; font-weight: 700; }
  .tagline { top: 352px; font-size: 13px; font-weight: 700; }
  .plans-heading {
    position: absolute; left: 79px; top: 382px; width: 465px; height: 53px;
    background: var(--slate); border-radius: 13px;
    font-family: "Roboto Condensed", "Arial Narrow", sans-serif;
    font-size: 30px; font-weight: 700; color: var(--ink-white);
    display: flex; align-items: center; justify-content: center; letter-spacing: 0.3px;
  }
  .plan-badge {
    position: absolute; left: 262px; width: 105px; height: 45px;
    background: var(--paper); border-radius: 8px;
    color: var(--brand-red); font-weight: 700;
    display: flex; align-items: center; justify-content: center;
  }
  .plan-badge .num { font-size: 24px; }
  .plan-badge .label { font-size: 14px; margin-top: 5px; }
  .plan-one { top: 461px; }
  .plan-two { top: 567px; }
  .plan-three { top: 669px; }
  .plan-text { font-size: 18.5px; font-weight: 700; line-height: 22px; }
  .plan-one-text { top: 524px; }
  .plan-two-text { top: 631px; }
  .plan-three-text { top: 733px; }
  .broker-photo {
    position: absolute; left: 21px; top: 680px; width: 92px; height: 122px;
    border: 3px solid var(--paper);
    background: linear-gradient(180deg, #8a8a7a 0%, #6d6a60 55%, #5a3a30 100%);
  }
  .broker-label {
    position: absolute; left: 0; top: 800px; width: 266px; height: 28px;
    background: var(--paper);
    display: flex; align-items: center; padding-left: 24px; font-size: 15px;
  }
  .broker-name { color: var(--brand-red); font-weight: 700; }
  .broker-role { color: var(--ink-dark); font-weight: 700; margin-left: 10px; font-size: 16px; }
  .social-links {
    position: absolute; left: 507px; top: 799px; display: flex; gap: 9px;
  }
  .social-links span {
    width: 19px; height: 19px; background: var(--paper); border-radius: 3px; display: block;
  }
  .contact-bar {
    position: absolute; left: 0; top: 823px; width: 628px; height: 64px;
    background: var(--slate);
    color: var(--ink-white);
  }
  .contact-line {
    position: absolute; left: 22px; display: flex; align-items: center; gap: 9px;
    font-size: 12px;
  }
  .contact-line svg { flex: none; }
  .address { top: 13px; }
  .website { top: 36px; }
  .bar-divider {
    position: absolute; left: 362px; top: 7px; width: 1px; height: 48px; background: #d8d8d8;
  }
  .phone {
    position: absolute; left: 376px; top: 12px;
    display: flex; align-items: center; gap: 12px;
    font-size: 31px; font-weight: 700;
  }
</style>
</head>
<body>
  <main class="flyer">
    <svg class="flyer-shapes" width="628" height="887" viewBox="0 0 628 887" aria-hidden="true">
      <defs>
        <radialGradient id="redGlow" cx="0.5" cy="0.28" r="0.7">
          <stop offset="0" stop-color="var(--brand-red-bright)"/>
          <stop offset="1" stop-color="var(--brand-red-deep)"/>
        </radialGradient>
      </defs>
      <path d="M0 329 Q314 275 628 338 L628 887 L0 887 Z" fill="url(#redGlow)"/>
      <path d="M0 560 Q300 440 628 470 L628 887 L0 887 Z" fill="#cc1a22" opacity="0.35"/>
      <path d="M118 300 Q314 280 520 302 Q314 292 118 300 Z" fill="var(--slate)" stroke="var(--slate)" stroke-width="3"/>
    </svg>

    <div class="hero-artwork" role="img" aria-label="Illustration of city buildings above a red house rooftop"></div>

    <h1 class="centered company-name">Summit Keystone Realty</h1>
    <p class="centered tagline">Your Key To Real Estate</p>

    <h2 class="plans-heading">OUR 3 COMMISSION PLANS</h2>

    <div class="plan-badge plan-one"><span class="num">1</span><span class="label">ST PLANE</span></div>
    <p class="centered plan-text plan-one-text">100% commision 99 dollars a month and $249 per transaction</p>

    <div class="plan-badge plan-two"><span class="num">2</span><span class="label">ND PLANE</span></div>
    <p class="centered plan-text plan-two-text">90/10 for $69 per month</p>

    <div class="plan-badge plan-three"><span class="num">3</span><span class="label">RD PLANE</span></div>
    <p class="centered plan-text plan-three-text">80/20 all planshave no office fees,<br>no franchise fees</p>

    <div class="broker-photo" role="img" aria-label="Portrait photo of the broker owner"></div>
    <div class="broker-label"><span class="broker-name">Marla Kessing ,</span><span class="broker-role">Broker Owner</span></div>

    <div class="social-links" aria-label="Social media links">
      <span></span><span></span><span></span><span></span>
    </div>

    <footer class="contact-bar">
      <p class="contact-line address">
        <svg width="11" height="15" viewBox="0 0 11 15"><path d="M5.5 0A5.5 5.5 0 0 0 0 5.5C0 9.5 5.5 15 5.5 15S11 9.5 11 5.5A5.5 5.5 0 0 0 5.5 0Zm0 7.7a2.2 2.2 0 1 1 0-4.4 2.2 2.2 0 0 1 0 4.4Z" fill="#fff"/></svg>
        4820 Elm Ridge Blvd, Garland, TX 75040 2nd floor 210
      </p>
      <p class="contact-line website">
        <svg width="12" height="12" viewBox="0 0 12 12"><circle cx="6" cy="6" r="5.3" fill="none" stroke="#fff" stroke-width="1.2"/><ellipse cx="6" cy="6" rx="2.3" ry="5.3" fill="none" stroke="#fff" stroke-width="1"/><path d="M0.8 6H11.2M1.6 3.3H10.4M1.6 8.7H10.4" stroke="#fff" stroke-width="0.9"/></svg>
        www.marlakessing.com
      </p>
      <span class="bar-divider"></span>
      <p class="phone">
        <svg width="22" height="22" viewBox="0 0 22 22"><path d="M5 2.5l3 3.5-1.8 2.2c1.2 2.6 3.2 4.6 5.8 5.8L14.2 12l3.5 3-1.6 3.2C9.4 18 4 12.6 3.7 4.2Z" fill="none" stroke="#fff" stroke-width="1.6" stroke-linejoin="round"/><path d="M13 2.5a7 7 0 0 1 6.5 6.5M13 5.5a4 4 0 0 1 3.5 3.5" fill="none" stroke="#fff" stroke-width="1.4"/></svg>
        214-555-0187
      </p>
    </footer>
  </main>
</body>
</html>
```